Trade Show Banner Stands

Looking for a fun, creative design to use for 2 banner stands - 85 X 200cm each, for an upcoming trade show in the biotech/pharma industry. We have a revolutionary product for use in the development of pharmaceutical drugs. Our equipment is unique and goals are to enhance our customers process development workflow, while maximizing their work space and generate more data with less operating and capital expenditures. Have included a file showing logo and color scheme and a couple photos for use. Website www.tovanu-bio.com. Interested in a innovative design that we can use and will amend wording once I start seeing designs. Thanks!

```html
<!DOCTYPE html>
<html lang="en">
<head>
<meta charset="utf-8">
<title>Tovanu Biosystems – Trade Show Banner Stands</title>
<link href="https://fonts.googleapis.com/css2?family=Montserrat:wght@400;500;700;800;900&display=swap" rel="stylesheet">
<style>
  :root {
    --navy: #283a6b;
    --navy-deep: #1f2f5c;
    --orange: #f26a21;
    --white: #ffffff;
    --ink: #2a3a70;
    --grey: #55565c;
    --backdrop: #000000;
  }
  html, body {
    margin: 0;
    padding: 0;
    width: 1031px;
    height: 1200px;
    overflow: hidden;
    background: var(--backdrop);
  }
  .stage {
    position: absolute;
    left: 0;
    top: 0;
    width: 1368px;
    height: 1592px;
    transform: scale(0.7537);
    transform-origin: 0 0;
    font-family: "Montserrat", sans-serif;
  }
  .banner {
    position: absolute;
    top: 94px;
    width: 562px;
    height: 1403px;
    overflow: hidden;
    background: var(--white);
  }
  .banner--left { left: 87px; }
  .banner--right { left: 718px; }
  .banner-shapes {
    position: absolute;
    left: 0;
    top: 0;
    width: 562px;
    height: 1403px;
  }
  .headline {
    position: absolute;
    left: 0;
    top: 38px;
    width: 562px;
    margin: 0;
    text-align: center;
    color: var(--white);
    font-weight: 900;
    text-transform: uppercase;
    line-height: 1;
  }
  .headline span { display: block; }
  .headline .l1 { font-size: 43px; letter-spacing: 0.5px; }
  .headline .l2 { font-size: 58px; margin-top: 14px; letter-spacing: 1px; }
  .headline .l3 { font-size: 43px; margin-top: 15px; }
  .headline .l4 { font-size: 45px; margin-top: 12px; }
  .benefit {
    position: absolute;
    color: var(--white);
    font-weight: 700;
    font-size: 25px;
    letter-spacing: 0.3px;
    line-height: 56px;
    height: 56px;
    white-space: nowrap;
  }
  .benefit--workflows { left: 15px; top: 300px; }
  .benefit--workspace { left: 246px; top: 392px; }
  .benefit--throughput { left: 13px; top: 484px; }
  .intro {
    position: absolute;
    left: 0;
    top: 906px;
    width: 562px;
    text-align: center;
    color: var(--ink);
  }
  .intro h2 {
    margin: 0;
    font-size: 38px;
    font-weight: 700;
    line-height: 48px;
  }
  .intro p {
    margin: 6px 0 0;
    font-size: 17.5px;
    font-weight: 500;
    line-height: 21px;
  }
  .product-photo {
    position: absolute;
    left: 50px;
    top: 1018px;
    width: 490px;
    height: 282px;
    border-radius: 10px;
    background: radial-gradient(ellipse at 50% 55%, #dfe1e5 0%, #eef0f2 55%, #ffffff 100%);
  }
  .brand {
    position: absolute;
    left: 0;
    top: 1280px;
    width: 562px;
    text-align: center;
  }
  .brand-name {
    display: block;
    margin-left: 20px;
    font-size: 58px;
    font-weight: 500;
    color: var(--grey);
    line-height: 70px;
    letter-spacing: 1px;
  }
  .brand-company {
    display: block;
    margin-left: 30px;
    font-size: 10.5px;
    font-weight: 700;
    color: var(--orange);
    line-height: 14px;
  }
  .brand-web {
    display: block;
    margin-left: 10px;
    font-size: 12.5px;
    font-weight: 500;
    color: var(--grey);
    line-height: 18px;
  }
</style>
</head>
<body>
<div class="stage">

  <section class="banner banner--left">
    <svg class="banner-shapes" viewBox="0 0 562 1403" aria-hidden="true">
      <defs>
        <linearGradient id="photoToneA" x1="0" y1="0" x2="1" y2="0.3">
          <stop offset="0" stop-color="#cdd5e0"/>
          <stop offset="0.45" stop-color="#a9b4c6"/>
          <stop offset="0.7" stop-color="#3fb3a8"/>
          <stop offset="1" stop-color="#1f9a8f"/>
        </linearGradient>
      </defs>
      <rect class="top-field" width="562" height="700" fill="var(--navy)"/>
      <path class="white-sweep" d="M0,560 C90,430 290,320 562,330 L562,1403 L0,1403 Z" fill="var(--white)"/>
      <path class="orange-swoosh" d="M0,820 Q260,960 562,620 L562,690 Q290,1010 0,870 Z" fill="var(--orange)"/>
      <path d="M22,530 C120,420 300,360 562,360 L562,640 Q280,945 0,830 L0,560 Z" fill="url(#photoToneA)" role="img" aria-label="Photo: gloved hand holding clear microfluidic perfusion chips in a lab"/>
    </svg>
    <svg class="banner-shapes" viewBox="0 0 562 1403" aria-hidden="true">
      <!-- benefit bars -->
      <rect x="0" y="300" width="380" height="56" fill="var(--orange)"/>
      <circle cx="373" cy="332" r="41" fill="var(--navy-deep)"/>
      <circle cx="368" cy="327" r="41" fill="var(--orange)"/>
      <g fill="none" stroke="var(--white)" stroke-width="3">
        <circle cx="378" cy="318" r="10"/><circle cx="378" cy="318" r="4"/>
        <circle cx="356" cy="330" r="7"/><circle cx="366" cy="344" r="6"/>
        <path d="M345,327 A26,26 0 0 1 392,306"/><path d="M393,332 A26,26 0 0 1 360,352"/>
      </g>
      <rect x="190" y="392" width="372" height="56" fill="var(--orange)"/>
      <circle cx="193" cy="424" r="41" fill="var(--navy-deep)"/>
      <circle cx="188" cy="419" r="41" fill="var(--orange)"/>
      <g fill="none" stroke="var(--white)" stroke-width="3.5" stroke-linecap="round">
        <path d="M185,398 L197,420"/><path d="M180,404 L192,426"/>
        <path d="M194,428 A16,16 0 0 1 178,442"/>
        <path d="M168,442 L210,442"/><path d="M176,420 L184,420"/>
      </g>
      <rect x="0" y="484" width="380" height="56" fill="var(--orange)"/>
      <circle cx="373" cy="516" r="41" fill="var(--navy-deep)"/>
      <circle cx="368" cy="511" r="41" fill="var(--orange)"/>
      <g fill="none" stroke="var(--white)" stroke-width="3">
        <rect x="340" y="500" width="56" height="28"/>
        <path d="M348,492 V524 M358,492 V524 M368,492 V524 M378,492 V524 M388,492 V524"/>
      </g>
    </svg>
    <h1 class="headline">
      <span class="l1">High Performance</span>
      <span class="l2">Automated</span>
      <span class="l3">True Perfusion</span>
      <span class="l4">Microbioreactors</span>
    </h1>
    <div class="benefit benefit--workflows">ENHANCE WORKFLOWS</div>
    <div class="benefit benefit--workspace">MAXIMIZE WORKSPACE</div>
    <div class="benefit benefit--throughput">IMPROVE THROUGHPUT</div>
    <div class="intro">
      <h2>What is Lorem Ipsum?</h2>
      <p>Lorem Ipsum is simply dummy text of the printing<br>and typesetting industry.</p>
    </div>
    <div class="product-photo" role="img" aria-label="Product photo: stacked microbioreactor units, media bottles and a laptop running control software"></div>
    <div class="brand">
      <span class="brand-name">tovanu</span>
      <span class="brand-company">Tovanu Biosystems, Inc</span>
      <span class="brand-web">www.tovanu-bio.com</span>
    </div>
  </section>

  <section class="banner banner--right">
    <svg class="banner-shapes" viewBox="0 0 562 1403" aria-hidden="true">
      <defs>
        <linearGradient id="photoToneB" x1="0" y1="0" x2="1" y2="0.3">
          <stop offset="0" stop-color="#cdd5e0"/>
          <stop offset="0.45" stop-color="#a9b4c6"/>
          <stop offset="0.7" stop-color="#3fb3a8"/>
          <stop offset="1" stop-color="#1f9a8f"/>
        </linearGradient>
      </defs>
      <rect class="top-field" width="562" height="700" fill="var(--navy)"/>
      <path class="white-sweep" d="M0,560 C90,430 290,320 562,330 L562,1403 L0,1403 Z" fill="var(--white)"/>
      <path class="orange-swoosh" d="M0,820 Q260,960 562,620 L562,690 Q290,1010 0,870 Z" fill="var(--orange)"/>
      <path d="M22,530 C120,420 300,360 562,360 L562,640 Q280,945 0,830 L0,560 Z" fill="url(#photoToneB)" role="img" aria-label="Photo: gloved hand holding clear microfluidic perfusion chips in a lab"/>
    </svg>
    <svg class="banner-shapes" viewBox="0 0 562 1403" aria-hidden="true">
      <rect x="0" y="300" width="380" height="56" fill="var(--orange)"/>
      <circle cx="373" cy="332" r="41" fill="var(--navy-deep)"/>
      <circle cx="368" cy="327" r="41" fill="var(--orange)"/>
      <g fill="none" stroke="var(--white)" stroke-width="3">
        <circle cx="378" cy="318" r="10"/><circle cx="378" cy="318" r="4"/>
        <circle cx="356" cy="330" r="7"/><circle cx="366" cy="344" r="6"/>
        <path d="M345,327 A26,26 0 0 1 392,306"/><path d="M393,332 A26,26 0 0 1 360,352"/>
      </g>
      <rect x="190" y="392" width="372" height="56" fill="var(--orange)"/>
      <circle cx="193" cy="424" r="41" fill="var(--navy-deep)"/>
      <circle cx="188" cy="419" r="41" fill="var(--orange)"/>
      <g fill="none" stroke="var(--white)" stroke-width="3.5" stroke-linecap="round">
        <path d="M185,398 L197,420"/><path d="M180,404 L192,426"/>
        <path d="M194,428 A16,16 0 0 1 178,442"/>
        <path d="M168,442 L210,442"/><path d="M176,420 L184,420"/>
      </g>
      <rect x="0" y="484" width="380" height="56" fill="var(--orange)"/>
      <circle cx="373" cy="516" r="41" fill="var(--navy-deep)"/>
      <circle cx="368" cy="511" r="41" fill="var(--orange)"/>
      <g fill="none" stroke="var(--white)" stroke-width="3">
        <rect x="340" y="500" width="56" height="28"/>
        <path d="M348,492 V524 M358,492 V524 M368,492 V524 M378,492 V524 M388,492 V524"/>
      </g>
    </svg>
    <h1 class="headline">
      <span class="l1">High Performance</span>
      <span class="l2">Automated</span>
      <span class="l3">True Perfusion</span>
      <span class="l4">Microbioreactors</span>
    </h1>
    <div class="benefit benefit--workflows">ENHANCE WORKFLOWS</div>
    <div class="benefit benefit--workspace">MAXIMIZE WORKSPACE</div>
    <div class="benefit benefit--throughput">IMPROVE THROUGHPUT</div>
    <div class="intro">
      <h2>What is Lorem Ipsum?</h2>
      <p>Lorem Ipsum is simply dummy text of the printing<br>and typesetting industry.</p>
    </div>
    <div class="product-photo" role="img" aria-label="Product photo: stacked microbioreactor units, media bottles and a laptop running control software"></div>
    <div class="brand">
      <span class="brand-name">tovanu</span>
      <span class="brand-company">Tovanu Biosystems, Inc</span>
      <span class="brand-web">www.tovanu-bio.com</span>
    </div>
  </section>

</div>
</body>
</html>
```